Flyer für Hersteller von Designertischen
Zielgruppe
Wir bauen Designer Tische, unser Zielgruppe liegt zwischen 35 und 50 Jahren
Aufgabenstellung
Wir legen Wert auf ein minimales Design, gerne in dem Stil unserer Website

```html
<!DOCTYPE html>
<html lang="de">
<head>
<meta charset="utf-8">
<title>Lindqvist Manufaktur – Flyer</title>
<link href="https://fonts.googleapis.com/css2?family=Montserrat:wght@300;400;500&display=swap" rel="stylesheet">
<style>
  :root {
    --stage: #e6e6e6;
    --paper: #f7f7f7;
    --paper-soft: #efefef;
    --ink: #3a3a3a;
    --ink-soft: #6b6b6b;
    --slate: #5f5f6e;
    --on-slate: #e9e9ee;
    --wall-light: #ecebea;
    --wall-mid: #d9d6d2;
    --floor: #cfc6ba;
    --wood: #a8794a;
    --mono-light: #b9b9b9;
    --mono-dark: #3c3c3c;
  }
  * { box-sizing: border-box; margin: 0; padding: 0; }
  html, body { width: 1200px; height: 900px; overflow: hidden; }
  body {
    background: var(--stage);
    font-family: "Montserrat", sans-serif;
    color: var(--ink);
    position: relative;
  }
  .brochure {
    position: absolute;
    left: 75px;
    width: 1050px;
    height: 360px;
    display: grid;
    grid-template-columns: repeat(3, 1fr);
    background: var(--paper);
    box-shadow: 0 10px 26px rgba(0,0,0,.12);
  }
  .brochure--outside { top: 60px; }
  .brochure--inside { top: 480px; }
  .panel { position: relative; overflow: hidden; border-right: 1px solid rgba(0,0,0,.05); }
  .panel:last-child { border-right: none; }

  .photo {
    position: absolute;
    background: linear-gradient(180deg, var(--wall-light) 0%, var(--wall-mid) 62%, var(--floor) 100%);
  }
  .photo--warm { background: linear-gradient(180deg, var(--wall-light) 0%, var(--wall-mid) 55%, var(--wood) 56%, var(--wall-mid) 62%, var(--floor) 100%); }
  .photo--mono { background: linear-gradient(160deg, var(--mono-light) 0%, #7a7a7a 55%, var(--mono-dark) 100%); }

  .heading {
    font-weight: 400;
    font-size: 15px;
    line-height: 1.25;
    letter-spacing: .01em;
    margin-bottom: 10px;
  }
  .copy {
    font-weight: 300;
    font-size: 9.5px;
    line-height: 1.55;
    color: var(--ink-soft);
  }

  /* outside spread */
  .vision-text { position: absolute; left: 20px; bottom: 24px; width: 130px; }
  .vision-photo { left: 140px; top: 0; right: 0; bottom: 0; }
  .values-text { position: absolute; left: 28px; top: 30px; right: 28px; }
  .values-photo { left: 0; right: 0; bottom: 0; height: 120px; }
  .hero-photo { inset: 0; }
  .hero-claim {
    position: absolute;
    right: 26px;
    bottom: 60px;
    font-weight: 300;
    font-size: 26px;
    line-height: 1.15;
    color: #ffffff;
    text-align: right;
  }

  /* brand */
  .brand {
    position: absolute;
    top: 16px;
    right: 18px;
    display: flex;
    align-items: center;
    gap: 6px;
    font-weight: 400;
    font-size: 10px;
    letter-spacing: .08em;
    color: var(--ink);
  }
  .brand-dot { width: 14px; height: 14px; border: 1px solid var(--ink); border-radius: 50%; }

  /* inside spread */
  .planning-photo { left: 0; top: 0; bottom: 0; width: 120px; }
  .planning-text { position: absolute; left: 140px; top: 110px; right: 22px; }
  .panel--slate { background: var(--slate); color: var(--on-slate); }
  .about-text { position: absolute; left: 150px; top: 28px; right: 22px; }
  .about-text .copy { color: var(--on-slate); }
  .about-photo { left: 0; bottom: 0; width: 135px; height: 190px; }
  .contact-photo { left: 0; top: 0; bottom: 0; width: 200px; }
  .contact-text { position: absolute; left: 218px; top: 120px; right: 14px; }
  .contact-list { list-style: none; font-weight: 300; font-size: 8.5px; line-height: 1.6; color: var(--ink-soft); }
</style>
</head>
<body>

<section class="brochure brochure--outside">
  <article class="panel">
    <div class="photo photo--warm vision-photo" role="img" aria-label="Foto: Tisch mit Holzplatte und schwarzem Stahlgestell vor heller Wand"></div>
    <div class="vision-text">
      <h2 class="heading">Unsere Vision</h2>
      <p class="copy">Unsere Vision bei der Lindqvist Manufaktur ist es, einen Beitrag zu leisten, der die Möbelbranche nachhaltig verändert. Wir möchten Möbel herstellen, die nicht nur funktional, sondern auch langlebig und schön sind. Unser Design verbindet Tradition mit moderner Formensprache und schafft Stücke, die Generationen begleiten.</p>
    </div>
  </article>
  <article class="panel">
    <div class="values-text">
      <h2 class="heading">Werte der<br>Lindqvist Manufaktur</h2>
      <p class="copy">Unsere Werte bilden das Fundament der Lindqvist Manufaktur. Gegenseitiger Respekt, Vertrauen und Ehrlichkeit stehen im Mittelpunkt unserer Arbeit. Wir verwenden ausschließlich Holz aus regionalen Wäldern und legen Wert auf sorgfältige Verarbeitung. Jeder Tisch erzählt die Geschichte seines Baumes und wird so zu einem einzigartigen Begleiter in Ihrem Zuhause.</p>
    </div>
  </article>
  <article class="panel">
    <div class="photo photo--warm hero-photo" role="img" aria-label="Foto: Bank aus Massivholz mit rostbraunen Stahlkufen"></div>
    <div class="brand"><span class="brand-dot"></span>Lindqvist</div>
    <p class="hero-claim">Möbel, die<br>Geschichten<br>erzählen.</p>
  </article>
</section>

<section class="brochure brochure--inside">
  <article class="panel">
    <div class="photo photo--warm planning-photo" role="img" aria-label="Foto: Tischecke mit Holzplatte und filigranem Stahlgestell"></div>
    <div class="planning-text">
      <h2 class="heading">Gemeinsame Planung</h2>
      <p class="copy">Gemeinsam mit dir gestalten wir dein individuelles Möbelstück. In einem persönlichen Gespräch erfassen wir deine Vorstellungen und Anforderungen. Basierend darauf entwickeln wir einen Entwurf, der Größe, Material und Stil vereint. Ziel ist es, ein Möbelstück zu bauen, das deine Erwartungen übertrifft.</p>
    </div>
  </article>
  <article class="panel panel--slate">
    <div class="photo photo--mono about-photo" role="img" aria-label="Schwarzweißfoto: Porträt des Gründers in einem Tunnel"></div>
    <div class="about-text">
      <h2 class="heading">Über mich</h2>
      <p class="copy">Ich bin Jonas Lindqvist und Gründer der Lindqvist Manufaktur. Mein Vater war Tischler, und so wuchs ich zwischen Holz und Werkzeug auf. Heute verbinde ich dieses Handwerk mit meiner Leidenschaft für klares Design. Jedes Stück entsteht in Stuttgart mit viel Sorgfalt und Liebe zum Detail.</p>
    </div>
  </article>
  <article class="panel">
    <div class="photo photo--warm contact-photo" role="img" aria-label="Foto: Beistelltisch aus Holz mit dunklem Stahlfuß"></div>
    <div class="brand"><span class="brand-dot"></span>Lindqvist</div>
    <div class="contact-text">
      <h2 class="heading">Kontakt</h2>
      <ul class="contact-list">
        <li>Lindqvist Manufaktur</li>
        <li>Kastanienweg 14</li>
        <li>70180 Stuttgart</li>
        <li>+49 1570 4412890</li>
        <li>lindqvist.manufaktur@mail.de</li>
      </ul>
    </div>
  </article>
</section>

</body>
</html>
```